Business Card Design Project

Business card design for an IT Service company. A logo has already been created in a different contest and has been attached to this project. Ideally we're looking for a double sided business card that matches the look and feel of our newly created logo.

We're open to creativity if you feel a tag line is needed such as "IT Services and Application Development". We're open to really and look and feel - even single sided business cards if you feel you have something that's a great idea.

Last thought here - I'm not sure how it'll look but maybe a two tone card? One side dark blue and the other side white? Don't limit the design submissions to this tho - just curious if it would look good

Nothing too busy please - simple... Thank you and happy designing!

Target Market(s)

Businesses that require IT Services and support for hosted services, technical consultation, web design.

Industry/Entity Type

Business

Font styles to use
Sans Serif

Requirements
Must have
• Use the colors provided in the logo (see attachment) or additional colors that compliment
Must have the following contact info (not necessarily in this order):
- Alan Fisk
- Founding Partner
- afisk@quillbarrow.example
- 555-382-1946
- www.quillbarrow.example

```html
<!DOCTYPE html>
<html lang="en">
<head>
<meta charset="utf-8">
<title>Quillbarrow Business Card</title>
<link href="https://fonts.googleapis.com/css2?family=Barlow:wght@300;400;600&family=Barlow+Semi+Condensed:wght@600&display=swap" rel="stylesheet">
<style>
  :root {
    --page: #e9e9e9;
    --navy: #1c2f5e;
    --blue-deep: #0b2b6b;
    --blue-mid: #1552a8;
    --blue-light: #2f86d4;
    --band-black: #050505;
    --green: #6a9a2c;
    --white: #ffffff;
    --paper: #f7f7f7;
  }
  * { margin: 0; padding: 0; box-sizing: border-box; }
  html, body { width: 927px; height: 1200px; overflow: hidden; background: var(--page); }
  body { position: relative; font-family: "Barlow", sans-serif; }

  .card {
    position: absolute;
    left: 114px;
    width: 700px;
    height: 400px;
    overflow: hidden;
    box-shadow: 0 6px 18px rgba(0,0,0,0.18);
  }
  .card--front { top: 150px; }
  .card--back { top: 650px; background: var(--paper); }

  .wave-field {
    position: absolute; inset: 0;
    background:
      radial-gradient(ellipse at 70% 30%, var(--blue-light) 0%, rgba(47,134,212,0) 55%),
      radial-gradient(ellipse at 20% 85%, #1f6cc0 0%, rgba(31,108,192,0) 60%),
      linear-gradient(160deg, var(--blue-mid) 0%, var(--blue-deep) 100%);
  }

  .front-band {
    position: absolute; left: 0; right: 0; top: 105px; height: 170px;
    background: var(--band-black);
    display: flex; align-items: center; justify-content: center; gap: 18px;
  }
  .brand-mark { width: 30px; height: 30px; background: var(--green); }
  .brand-name {
    font-family: "Barlow Semi Condensed", sans-serif;
    font-weight: 600; font-size: 62px; letter-spacing: 0.5px;
    color: var(--white);
  }

  .back-head {
    position: absolute; left: 0; right: 0; top: 0; height: 208px;
    display: flex; align-items: center; justify-content: center; gap: 18px;
  }
  .back-head .brand-name { color: var(--navy); }
  .back-head .brand-mark { background: var(--green); }

  .back-rule { position: absolute; left: 0; right: 0; top: 208px; height: 6px; background: var(--green); }
  .back-foot { position: absolute; left: 0; right: 0; top: 214px; bottom: 0; }

  .person { position: absolute; left: 36px; top: 252px; color: var(--white); }
  .person-name { font-weight: 600; font-size: 24px; }
  .person-role { font-weight: 300; font-size: 20px; margin-top: 2px; }

  .contact-list {
    position: absolute; left: 388px; top: 264px; list-style: none; color: var(--white);
  }
  .contact-item { display: flex; align-items: center; gap: 10px; font-size: 20px; height: 30px; }
  .contact-icon {
    width: 18px; height: 18px; border-radius: 4px; background: var(--green);
    display: flex; align-items: center; justify-content: center; flex: none;
  }
  .contact-icon svg { width: 12px; height: 12px; }
</style>
</head>
<body>

  <section class="card card--front" aria-label="Card front">
    <div class="wave-field" role="img" aria-label="Blue background with flowing light wave lines"></div>
    <div class="front-band">
      <span class="brand-mark"></span>
      <span class="brand-name">Quillbarrow</span>
    </div>
  </section>

  <section class="card card--back" aria-label="Card back">
    <div class="back-head">
      <span class="brand-mark"></span>
      <span class="brand-name">Quillbarrow</span>
    </div>
    <div class="back-rule"></div>
    <div class="back-foot wave-field" role="img" aria-label="Blue background with flowing light wave lines"></div>

    <div class="person">
      <p class="person-name">Alan Fisk</p>
      <p class="person-role">Founding Partner</p>
    </div>

    <ul class="contact-list">
      <li class="contact-item">
        <span class="contact-icon"><svg viewBox="0 0 12 12"><rect x="1" y="2.5" width="10" height="7" fill="none" stroke="#fff" stroke-width="1.3"/><path d="M1 3 L6 7 L11 3" fill="none" stroke="#fff" stroke-width="1.3"/></svg></span>
        afisk@quillbarrow.example
      </li>
      <li class="contact-item">
        <span class="contact-icon"><svg viewBox="0 0 12 12"><path d="M3 1 L5 3.5 L4 5 Q5 7 7 8 L8.5 7 L11 9 L9.5 11 Q4 10.5 1 3 Z" fill="#fff"/></svg></span>
        555-382-1946
      </li>
      <li class="contact-item">
        <span class="contact-icon"><svg viewBox="0 0 12 12"><circle cx="6" cy="6" r="4.5" fill="none" stroke="#fff" stroke-width="1.2"/><path d="M1.5 6 H10.5 M6 1.5 Q3.5 6 6 10.5 M6 1.5 Q8.5 6 6 10.5" fill="none" stroke="#fff" stroke-width="1"/></svg></span>
        www.quillbarrow.example
      </li>
    </ul>
  </section>

</body>
</html>
```